Ranked amongst the Best Colleges and Programs

the size of the ad is Full Page, with bleed*
8”x 10.75" plus 0.25" bleed'
you have two choices for the tagline .. please chose what ever you think will allow you to make a better ad.
The instructions on the brief are in red
I am looking for a hight quality modern ad to place in local weekly publications that will stand out .
I would like a ad that people will look at and say i would like to see what this ad is all about.
I apprecate creative work.
the ad should not be very crowded and the text should be able to be read.
if you decide to use people in the ad .. (you don't have to ) then it should be a male dressed in white shirt in and sports jacket.. or if you would like you can use a vector and then use male or female people.
please leave one inch on the bottom for the footer

Target Market(s)

potential middle class students from 23-35 years of age

Industry/Entity Type

education

Requirements
Must have
• .the " 98% employment rate" should stand out in the ad.. but should not be the main part of the ad
Nice to have
• creative
Should not have
• Should not be a very busy or crowded ad.. i prefer pictures of men but should be .. in a business suit .. that looks professional- white shirt

```html
<!DOCTYPE html>
<html lang="en">
<head>
<meta charset="UTF-8">
<title>Get ahead faster in your career</title>
<link rel="stylesheet" href="https://fonts.googleapis.com/css2?family=Archivo+Black&family=Figtree:wght@400;500;700;800&display=swap">
<style>
  :root {
    --cyan: #00ffff;
    --navy-deep: #0a0f5c;
    --navy: #0b1a6e;
    --blue-mid: #0a3d8f;
    --orange: #f2600a;
    --orange-core: #ff9a10;
    --gold: #f5b400;
    --white: #ffffff;
    --ink: #0b0a33;
    --grid-line: rgba(190, 180, 120, 0.55);
  }
  * { margin: 0; padding: 0; box-sizing: border-box; }
  html, body { width: 900px; height: 1200px; overflow: hidden; background: var(--cyan); }
  .ad {
    position: relative;
    width: 900px;
    height: 1200px;
    background: var(--cyan);
    font-family: "Figtree", sans-serif;
    color: var(--white);
    overflow: hidden;
  }
  .page {
    position: absolute;
    left: 26px;
    top: 0;
    width: 848px;
    height: 1200px;
    overflow: hidden;
    background:
      radial-gradient(ellipse 60% 40% at 85% 90%, rgba(0, 90, 140, 0.5), transparent 70%),
      linear-gradient(180deg, #033a85 0%, #061a78 25%, var(--navy-deep) 55%, #051a5c 75%, #041a4a 100%);
    box-shadow: inset 0 0 40px rgba(0, 255, 255, 0.35);
  }
  .grid {
    position: absolute;
    inset: 0 0 auto 0;
    height: 940px;
    background-image:
      linear-gradient(to right, var(--grid-line) 1px, transparent 1px),
      linear-gradient(to bottom, var(--grid-line) 1px, transparent 1px);
    background-size: 42.4px 42.4px;
    background-position: 14px 0;
    -webkit-mask-image: linear-gradient(180deg, #000 0%, #000 50%, rgba(0,0,0,0.25) 80%, transparent 100%);
    mask-image: linear-gradient(180deg, #000 0%, #000 50%, rgba(0,0,0,0.25) 80%, transparent 100%);
  }
  .sun {
    position: absolute;
    left: 218px;
    top: 128px;
    width: 412px;
    height: 412px;
    border-radius: 50%;
    background: radial-gradient(circle at 55% 48%, var(--orange-core) 0%, #f7800c 30%, var(--orange) 70%);
    box-shadow: 0 0 40px 14px rgba(170, 70, 150, 0.55);
  }
  .headline {
    position: absolute;
    left: 0;
    top: 252px;
    width: 848px;
    text-align: center;
    font-family: "Archivo Black", sans-serif;
    font-size: 80px;
    line-height: 82px;
    letter-spacing: -0.5px;
    color: var(--white);
    text-shadow: 3px 4px 0 var(--ink);
  }
  .subline {
    position: absolute;
    left: 0;
    top: 438px;
    width: 848px;
    text-align: center;
    font-size: 17px;
    font-weight: 500;
    color: var(--cyan);
    text-shadow: 1px 1px 0 var(--ink);
  }
  .award-icon {
    position: absolute;
    left: 394px;
    top: 618px;
    width: 60px;
    height: 82px;
  }
  .rankings {
    position: absolute;
    left: 0;
    top: 718px;
    width: 848px;
    text-align: center;
  }
  .rankings-title {
    font-size: 17px;
    font-weight: 700;
    text-decoration: underline;
    text-underline-offset: 3px;
    margin-bottom: 8px;
  }
  .rankings-item { font-size: 14px; line-height: 20px; }
  .horizon {
    position: absolute;
    left: 0;
    top: 858px;
    width: 848px;
    height: 342px;
  }
  .stat {
    position: absolute;
    left: 0;
    top: 905px;
    width: 848px;
    text-align: center;
    color: var(--gold);
  }
  .stat-figure {
    font-family: "Figtree", sans-serif;
    font-weight: 800;
    font-size: 118px;
    line-height: 112px;
    letter-spacing: -2px;
  }
  .stat-label {
    font-weight: 700;
    font-size: 24px;
    letter-spacing: 0.3px;
    margin-top: 2px;
  }
  .outcomes {
    position: absolute;
    left: 0;
    top: 1092px;
    width: 848px;
    text-align: center;
    font-size: 15.5px;
    line-height: 22px;
    font-weight: 500;
  }
</style>
</head>
<body>
<div class="ad">
  <div class="page">
    <div class="grid"></div>
    <div class="sun"></div>

    <h1 class="headline">Get ahead faster<br>in your career</h1>
    <p class="subline">With a prestigious NRU- Masters of Accounting Degree.</p>

    <svg class="award-icon" viewBox="0 0 60 82" fill="none" stroke="#8a8fc0" stroke-width="1.6" stroke-linejoin="round">
      <circle cx="30" cy="28" r="26" stroke-dasharray="4 2"/>
      <circle cx="30" cy="28" r="21"/>
      <circle cx="30" cy="28" r="15"/>
      <path d="M30 18 l3 7 7.5 .5 -5.8 4.8 1.9 7.3 -6.6-4.1 -6.6 4.1 1.9-7.3 -5.8-4.8 7.5-.5z"/>
      <path d="M16 50 L2 74 L13 71 L18 82 L28 56"/>
      <path d="M44 50 L58 74 L47 71 L42 82 L32 56"/>
    </svg>

    <div class="rankings">
      <p class="rankings-title">Ranked amongst:</p>
      <p class="rankings-item">Best Colleges-Fenwick 2023</p>
      <p class="rankings-item">Best Masters in Accounting Degree - Edunova 2023</p>
    </div>

    <svg class="horizon" viewBox="0 0 848 342" preserveAspectRatio="none">
      <defs>
        <linearGradient id="horizonFill" x1="0" y1="0" x2="1" y2="1">
          <stop offset="0" stop-color="#0560b0"/>
          <stop offset="0.3" stop-color="#0a2a95"/>
          <stop offset="0.7" stop-color="#0a3a8a"/>
          <stop offset="1" stop-color="#18d6d6"/>
        </linearGradient>
      </defs>
      <path d="M0 186 C150 50 310 0 424 0 C540 0 700 50 848 186 L848 342 L0 342 Z" fill="url(#horizonFill)"/>
    </svg>

    <div class="stat">
      <p class="stat-figure">98%</p>
      <p class="stat-label">EMPLOYMENT RATE</p>
    </div>

    <p class="outcomes">BCS graduates have gone on to work in various high-quality jobs in top firms,<br>earning impressive six-figure salaries as well as opening successful businesses.</p>
  </div>
</div>
</body>
</html>
```